Oversized Post Card for Busines Owners 1st 2nd and 3rd prizes

Create a professional, fresh and polished oversized post card for law firm specializing in Business Law, Succession Planning, and Employment Law

Use any picture(s) of your choice (mine or ones you recommend), logo, headshot and company info

www.morvenquaylegal.example

Westbrook Office - 4175 Hollister Avenue, Suite 1400, Charlotte, NC 28299
Kestrelmoor Office - 13840 Tamsin Way, Suite 300, Charlotte, NC 28296

Phone (704) 555-0187

Use this card for a Free Consultation

Target Market(s)

Business Owners (of small businesses)

Industry/Entity Type

Business

Font styles to use
Serif
Sans Serif

Requirements
Must have
• Company name, logo and contact info
• Serving business owners with legal guidance
• Business Law, Succession Planning & Wealth Transfers
• www.morvenquaylegal.example
• Westbrook Office - 4175 Hollister Avenue, Suite 1400, Charlotte, NC 28299
• Kestrelmoor Office - 13840 Tamsin Way, Suite 300, Charlotte, NC 28296
• Phone (704) 555-0187
• Use this card for a Free Consultation
Nice to have
• pictures (yours or mine) - you choose; headshot picture

```html
<!DOCTYPE html>
<html lang="en">
<head>
<meta charset="utf-8">
<title>Morven Quay Law, PLLC – Free Consultation Postcard</title>
<link rel="stylesheet" href="https://fonts.googleapis.com/css2?family=Oswald:wght@500&family=Roboto+Condensed:wght@400;500&family=Old+Standard+TT:wght@400&display=swap">
<style>
  :root {
    --teal: #117489;
    --teal-text: #1a7286;
    --banner-grey: #969292;
    --band-grey: #ecebeb;
    --ink: #111111;
    --paper: #ffffff;
    --city-deep: #2b2a6e;
    --city-mid: #5a4a9c;
    --city-glow: #c98a4a;
  }
  * { margin: 0; padding: 0; box-sizing: border-box; }
  html, body { width: 1200px; height: 777px; overflow: hidden; background: var(--paper); }
  .postcard { position: relative; width: 1200px; height: 777px; overflow: hidden; background: var(--paper); }

  .grey-band { position: absolute; left: 0; top: 193px; width: 1200px; height: 147px;
    background: linear-gradient(180deg, #f3f3f3 0%, var(--band-grey) 100%); }
  .header { position: absolute; left: 0; top: 0; width: 1004px; height: 236px;
    background: linear-gradient(180deg, #ffffff 0%, #f1f1f1 100%); }

  .brand-mark { position: absolute; left: 176px; top: 31px; width: 111px; height: 111px; border-radius: 50%; background: var(--teal); }
  .brand-rule { position: absolute; left: 67px; top: 153px; width: 328px; height: 2px; background: var(--ink); }
  .brand-name { position: absolute; left: 67px; top: 160px; width: 328px; text-align: center;
    font-family: "Old Standard TT", serif; font-weight: 400; color: var(--teal);
    font-size: 38px; letter-spacing: 1px; line-height: 40px; white-space: nowrap; }
  .brand-sub { position: absolute; left: 67px; top: 199px; width: 328px; height: 20px;
    display: flex; align-items: center; gap: 12px;
    font-family: "Old Standard TT", serif; font-weight: 400; color: var(--ink); font-size: 17px; white-space: nowrap; }
  .brand-sub::before, .brand-sub::after { content: ""; flex: 1; height: 2px; background: var(--ink); }

  .contact { position: absolute; left: 463px; top: 36px; font-family: "Roboto Condensed", sans-serif; }
  .contact-rule { position: absolute; left: 0; top: 2px; width: 4px; height: 132px; background: var(--ink); }
  .office { padding-left: 17px; margin-bottom: 8px; }
  .office-name { color: var(--teal-text); font-size: 23px; font-weight: 500; line-height: 26px; }
  .office-address { color: var(--ink); font-size: 19px; font-weight: 500; line-height: 24px; padding-left: 18px; white-space: nowrap; }
  .contact-line { position: absolute; left: 15px; top: 128px; white-space: nowrap; font-size: 19px; font-weight: 500; }
  .contact-line .label { color: var(--teal-text); }
  .contact-line .phone { color: var(--ink); margin-right: 36px; }
  .contact-line .web { color: var(--teal-text); }

  .offer-banner { position: absolute; left: 0; top: 237px; width: 797px; height: 92px; }
  .offer-text { position: absolute; left: 26px; top: 237px; height: 92px; line-height: 92px;
    font-family: "Oswald", sans-serif; font-weight: 500; font-size: 49px; color: var(--paper); white-space: nowrap; }

  .services { position: absolute; left: 0; top: 340px; width: 796px; height: 330px; background: var(--teal);
    color: var(--paper); font-family: "Old Standard TT", serif; }
  .services-intro { position: absolute; left: 31px; top: 11px; font-size: 25px; white-space: nowrap; }
  .services-list { position: absolute; left: 66px; top: 56px; list-style: none; font-size: 25px; }
  .services-list li { position: relative; padding-left: 16px; height: 33px; line-height: 33px; white-space: nowrap; }
  .services-list li::before { content: ""; position: absolute; left: 0; top: 13px; width: 9px; height: 9px;
    border-radius: 50%; background: var(--paper); }

  .skyline { position: absolute; left: 0; top: 607px; width: 518px; height: 170px;
    background: linear-gradient(180deg, var(--city-deep) 0%, var(--city-mid) 45%, var(--city-glow) 100%); }
</style>
</head>
<body>
<main class="postcard">
  <div class="grey-band"></div>
  <header class="header">
    <span class="brand-mark" aria-hidden="true"></span>
    <span class="brand-rule" aria-hidden="true"></span>
    <div class="brand-name">MORVEN QUAY</div>
    <div class="brand-sub">LAW, PLLC</div>
    <div class="contact">
      <span class="contact-rule"></span>
      <div class="office">
        <div class="office-name">Westbrook Office</div>
        <div class="office-address">4175 Hollister Avenue, Suite 1400, Charlotte, NC 28299</div>
      </div>
      <div class="office">
        <div class="office-name">Kestrelmoor Office</div>
        <div class="office-address">13840 Tamsin Way, Suite 300, Charlotte, NC 28296</div>
      </div>
      <div class="contact-line">
        <span class="label">Phone:</span> <span class="phone">(704) 555-0187</span>
        <span class="web">www.morvenquaylegal.example</span>
      </div>
    </div>
  </header>

  <svg class="offer-banner" viewBox="0 0 797 92" aria-hidden="true">
    <polygon points="0,0 757,0 797,46 757,92 0,92" fill="var(--banner-grey)"/>
  </svg>
  <div class="offer-text">Use this card for a Free Consultation</div>

  <section class="services">
    <p class="services-intro">Serving business owners with legal guidance, which may include:</p>
    <ul class="services-list">
      <li>Business Law</li>
      <li>Succession Planning and Wealth Transfers</li>
      <li>Last Will and Testament</li>
      <li>Revocable Trusts and Irrevocable Trusts</li>
      <li>Powers of Attorney and Living Wills</li>
      <li>Life Insurance</li>
    </ul>
  </section>

  <div class="skyline" role="img" aria-label="Night photograph of the Charlotte city skyline with lit towers"></div>
</main>
</body>
</html>
```